Business Card and Letterhead for new company Corvalt GreenWorks, Inc.

Corvalt GreenWorks, Inc., an engineering and construction firm that provides services for solid waste landfill gas systems, needs a business card and letterhead. We recently had a logo designed but we are open to some tweaks to logo design and color scheme. Generally, we like "earthy" color tones - greens, browns, oranges. This is a sister company - www.taldrickengineering.example.

Target Market(s)

Solid waste landfill companies - Binford Disposal, Keystell Holdings, etc.

Industry/Entity Type

Engineering and Construction

Contact Information for Business Card

Name, Title, email, mobile phone, work phone, website. Potential list of services for back of card: LFG Engineering and Design, GCCS Planning and Operational Consulting, Compliance Monitoring and Reporting, Routine Operations & Maintenance, Nonroutine O&M, Construction Management, Construction QA, GCCS Construction

Font styles to use
Sans Serif

Requirements
Must have
• Logo, pertinent information, maybe a tagline (still in development)
Nice to have
• For back of card, considering an engineering scale (attached for another business of ours), but want to look at other options, alternatives. Like the idea of the back of card to have some utility (scale, unit conversion info, list of services) but willing to consider lots of options.
Should not have
• Needs to have a professional (engineering) and technical look, not cartoonish.

```html
<!DOCTYPE html>
<html lang="en">
<head>
<meta charset="utf-8">
<title>Corvalt GreenWorks — Stationery</title>
<link href="https://fonts.googleapis.com/css2?family=Arimo:wght@400;700&display=swap" rel="stylesheet">
<style>
  :root {
    --stage: #000000;
    --paper: #ffffff;
    --green: #6db33f;
    --teal: #2a8fb0;
    --orange: #f08a1c;
    --ink: #5a5a5a;
    --mark-faint: #f1f4f1;
  }
  * { box-sizing: border-box; margin: 0; padding: 0; }
  html, body { width: 1200px; height: 1200px; overflow: hidden; background: var(--stage); }
  body { position: relative; font-family: "Arimo", Arial, sans-serif; }

  .letterhead, .card { position: absolute; background: var(--paper); box-shadow: 0 6px 18px rgba(255,255,255,0.08); overflow: hidden; }
  .letterhead { left: 94px; top: 72px; width: 744px; height: 1053px; }
  .card-front { left: 571px; top: 232px; width: 535px; height: 314px; box-shadow: 0 8px 16px rgba(0,0,0,0.35); }
  .card-back { left: 571px; top: 582px; width: 535px; height: 313px; background: linear-gradient(90deg, #78b843 0%, #5ea77a 50%, #2a8fb0 100%); box-shadow: 0 8px 16px rgba(0,0,0,0.35); }

  .brand { position: absolute; display: flex; align-items: center; gap: 12px; color: var(--green); font-weight: 700; white-space: nowrap; }
  .brand-dot { border-radius: 50%; background: var(--teal); flex: none; }
  .letterhead .brand { left: 56px; top: 70px; font-size: 34px; }
  .letterhead .brand-dot { width: 40px; height: 40px; }
  .card-front .brand { left: 36px; top: 40px; font-size: 28px; }
  .card-front .brand-dot { width: 32px; height: 32px; }

  .rule { position: absolute; }
  .watermark { position: absolute; border-radius: 50%; }
  .letterhead .watermark { left: 192px; top: 438px; width: 380px; height: 380px; border: 34px solid var(--mark-faint); }
  .card-back .watermark { left: 360px; top: 87px; width: 150px; height: 150px; border: 14px solid rgba(255,255,255,0.14); }

  .contacts { position: absolute; list-style: none; text-align: right; color: var(--ink); }
  .contacts li { display: flex; justify-content: flex-end; align-items: center; gap: 8px; }
  .contacts svg { width: 10px; height: 10px; flex: none; }
  .letterhead .contacts { right: 46px; top: 928px; font-size: 14.5px; line-height: 22.5px; }
  .card-front .contacts { right: 40px; top: 180px; font-size: 15px; line-height: 24.5px; }

  .person { position: absolute; left: 36px; top: 182px; }
  .person-name { color: var(--teal); font-weight: 700; font-size: 24px; line-height: 1; }
  .person-title { color: var(--ink); font-size: 15px; margin-top: 7px; }

  .services { position: absolute; left: 44px; top: 60px; list-style: none; color: #fff; font-size: 14px; line-height: 24.6px; }
  .services li { display: flex; align-items: center; gap: 8px; }
  .services li::before { content: ""; width: 6px; height: 8px; background: var(--orange); border-radius: 50% 50% 50% 50% / 65% 65% 35% 35%; }
</style>
</head>
<body>

<section class="letterhead" aria-label="Letterhead">
  <div class="watermark" aria-hidden="true"></div>
  <div class="brand"><span class="brand-dot"></span>Corvalt GreenWorks</div>
  <svg class="rule" style="left:672px;top:50px" width="40" height="860" aria-hidden="true">
    <path d="M3 3 H34 V858" fill="none" stroke="var(--teal)" stroke-width="5"/>
  </svg>
  <svg class="rule" style="left:33px;top:998px" width="430" height="20" aria-hidden="true">
    <path d="M3 17 V8 H428" fill="none" stroke="var(--green)" stroke-width="5"/>
  </svg>
  <ul class="contacts">
    <li>555-014-2270 <svg viewBox="0 0 10 10"><path d="M2 1 L4 1 L4.6 3.4 L3.4 4.2 Q4.6 6 6 6.6 L6.8 5.4 L9 6 L9 8 Q5 9 2.2 6.4 Q0.6 4 2 1Z" fill="var(--orange)"/></svg></li>
    <li>555-019-3384 <svg viewBox="0 0 10 10"><rect x="2.5" y="0.5" width="5" height="9" rx="1" fill="none" stroke="var(--orange)" stroke-width="1.2"/></svg></li>
    <li>info@corvaltgreenworks.example <svg viewBox="0 0 10 10"><rect x="0.5" y="2" width="9" height="6.5" fill="var(--orange)"/><path d="M0.5 2 L5 5.6 L9.5 2" fill="none" stroke="#fff" stroke-width="0.9"/></svg></li>
    <li>www.corvaltgreenworks.example <svg viewBox="0 0 10 10"><circle cx="5" cy="5" r="4.2" fill="none" stroke="var(--orange)" stroke-width="1.4"/><circle cx="5" cy="5" r="1.6" fill="var(--orange)"/></svg></li>
  </ul>
</section>

<section class="card card-front" aria-label="Business card front">
  <div class="brand"><span class="brand-dot"></span>Corvalt GreenWorks</div>
  <svg class="rule" style="left:473px;top:26px" width="40" height="128" aria-hidden="true">
    <path d="M3 125 V3 H37" fill="none" stroke="var(--teal)" stroke-width="4.5"/>
  </svg>
  <div class="person">
    <p class="person-name">YOUR NAME</p>
    <p class="person-title">Designation</p>
  </div>
  <svg class="rule" style="left:36px;top:262px" width="202" height="22" aria-hidden="true">
    <path d="M3 20 V6 H200" fill="none" stroke="var(--green)" stroke-width="4.5"/>
  </svg>
  <ul class="contacts">
    <li>555-014-2270 <svg viewBox="0 0 10 10"><path d="M2 1 L4 1 L4.6 3.4 L3.4 4.2 Q4.6 6 6 6.6 L6.8 5.4 L9 6 L9 8 Q5 9 2.2 6.4 Q0.6 4 2 1Z" fill="var(--orange)"/></svg></li>
    <li>555-019-3384 <svg viewBox="0 0 10 10"><rect x="2.5" y="0.5" width="5" height="9" rx="1" fill="none" stroke="var(--orange)" stroke-width="1.2"/></svg></li>
    <li>info@corvaltgreenworks.example <svg viewBox="0 0 10 10"><rect x="0.5" y="2" width="9" height="6.5" fill="var(--orange)"/><path d="M0.5 2 L5 5.6 L9.5 2" fill="none" stroke="#fff" stroke-width="0.9"/></svg></li>
    <li>www.corvaltgreenworks.example <svg viewBox="0 0 10 10"><circle cx="5" cy="5" r="4.2" fill="none" stroke="var(--orange)" stroke-width="1.4"/><circle cx="5" cy="5" r="1.6" fill="var(--orange)"/></svg></li>
  </ul>
</section>

<section class="card card-back" aria-label="Business card back">
  <div class="watermark" aria-hidden="true"></div>
  <ul class="services">
    <li>LFG Engineering and Design</li>
    <li>GCCS Planning and Operational Consulting</li>
    <li>Compliance Monitoring and Reporting</li>
    <li>Routine Operations &amp; Maintenance</li>
    <li>Nonroutine O&amp;M</li>
    <li>Construction Management</li>
    <li>Construction QA</li>
    <li>GCCS Construction</li>
  </ul>
</section>

</body>
</html>
```